Utility Contractor looking for a new website

Water and wastewater utility contractor looking to create a new website that highlights our various services. We are looking for modern web presence that can be updated with current projects and new services as we grow. We have an existing logo that we would like to incorporate into the overall design of the site
Updates

Hi, Thank you for all the design submissions. I have had some time to review and have eliminated the ones I feel are not what I am looking for. Based on the designs that remain, I am looking for a clean (not to many bold colours), modern look that is not to busy (long scrolling page), Thanks, Dean

Target Market(s)

project managers, strata boards, owners, people who make decisions as to who operates their water/wastewater system

Industry/Entity Type

Utility

Font styles to use
Sans Serif

Requirements
Must have
• A min page that describes the company and what we do, A page for each of our services that outlines the service and the benefits of it. the look must be consistent throughout. additionally each service page should have some images related to the service

```html
<!DOCTYPE html>
<html lang="en">
<head>
<meta charset="utf-8">
<title>Clearline Waterworks Ltd. – Water &amp; Wastewater System Operation</title>
<link href="https://fonts.googleapis.com/css2?family=Hind:wght@300;400;600&display=swap" rel="stylesheet">
<style>
  :root {
    --page-bg: #e8e8e8;
    --panel-bg: #ffffff;
    --panel-border: #d6d6d6;
    --panel-frame: #f1f1f1;
    --navy: #0e2d52;
    --green: #149a5a;
    --text: #2b2b2b;
    --nav-text: #444444;
    --nav-active: #2f6fb4;
    --hero-start: #0a5f92;
    --hero-end: #1bbff0;
    --photo-frame: #1d5f8e;
  }
  * { box-sizing: border-box; margin: 0; padding: 0; }
  html, body {
    width: 1171px; height: 1200px; overflow: hidden;
    background: var(--page-bg);
    font-family: "Hind", Arial, sans-serif;
    color: var(--text);
  }
  .site { position: relative; width: 1171px; height: 1200px; }

  .site-header {
    position: absolute; left: 115px; top: 22px; width: 941px; height: 80px;
  }
  .brand {
    position: absolute; left: 2px; top: 26px;
    display: flex; align-items: center; gap: 12px;
    font-weight: 400; font-size: 30px; line-height: 36px;
    color: var(--navy);
  }
  .brand-dot {
    width: 22px; height: 22px; border-radius: 50%; background: var(--navy);
  }
  .call-now {
    position: absolute; right: 0; top: 38px;
    font-size: 30px; font-weight: 400; color: #1d1d1d; line-height: 40px;
  }
  .call-now .phone { color: var(--green); font-size: 34px; }

  .main-nav {
    position: absolute; left: 115px; top: 119px; width: 941px; height: 48px;
    background: var(--panel-frame); border: 1px solid var(--panel-border);
    padding: 7px 8px;
  }
  .main-nav ul {
    list-style: none; display: flex; justify-content: space-around;
    background: var(--panel-bg); height: 33px; align-items: center;
    padding: 0 12px;
  }
  .main-nav a {
    text-decoration: none; color: var(--nav-text); font-size: 15px; font-weight: 400;
  }
  .main-nav a.current { color: var(--nav-active); }

  .content-panel {
    position: absolute; left: 115px; top: 175px; width: 941px; height: 909px;
    background: var(--panel-frame); border: 1px solid var(--panel-border);
    padding: 8px;
  }
  .content-inner {
    background: var(--panel-bg); height: 100%; padding: 9px 9px 0 9px;
  }
  .page-hero {
    height: 133px;
    background: linear-gradient(100deg, var(--hero-start) 0%, #0a8ccc 45%, #08b0ea 85%, var(--hero-end) 100%);
    display: flex; align-items: center; padding-left: 23px;
  }
  .page-hero h1 {
    color: #fff; font-weight: 400; font-size: 35px; letter-spacing: -0.3px; padding-top: 6px;
  }
  .service-block {
    font-size: 15.1px; line-height: 21.5px; font-weight: 300;
    hyphens: auto; -webkit-hyphens: auto;
  }
  .service-block p { margin-bottom: 15px; }
  .service-block p:last-of-type { margin-bottom: 0; }
  .service-block.first { margin-top: 36px; }
  .service-block.second { margin-top: 44px; }
  .service-block::after { content: ""; display: block; clear: both; }
  .service-photo {
    width: 372px; height: 259px; border: 3px solid var(--photo-frame);
  }
  .service-photo.right { float: right; margin: 0 0 8px 24px; background: linear-gradient(160deg, #d7d9d8, #b9bcc0 55%, #6f86b4); }
  .service-photo.left { float: left; margin: 0 18px 8px 1px; background: linear-gradient(150deg, #5e6a63, #3f7c4c 50%, #8a8f8c); }

  .water-band {
    position: absolute; left: 0; bottom: 0; width: 1171px; height: 68px;
    background: linear-gradient(180deg, #e8e8e8 0%, #b6c8d6 18%, #6f92ad 32%, #c9d8e2 60%, #e4e9ed 100%);
  }
</style>
</head>
<body>
<div class="site">
  <header class="site-header">
    <div class="brand"><span class="brand-dot"></span><span>Clearline Waterworks Ltd.</span></div>
    <div class="call-now">Call Now: <span class="phone">250 555-0142</span></div>
  </header>

  <nav class="main-nav">
    <ul>
      <li><a href="#">Home</a></li>
      <li><a href="#">About Us</a></li>
      <li><a href="#" class="current">System Operation</a></li>
      <li><a href="#">Fire Hydrant Maintenance</a></li>
      <li><a href="#">Backflow Device Testing</a></li>
      <li><a href="#">Contact Us</a></li>
    </ul>
  </nav>

  <main class="content-panel">
    <div class="content-inner">
      <section class="page-hero"><h1>Water &amp; Wastewater System Operation</h1></section>

      <section class="service-block first">
        <div class="service-photo right" role="img" aria-label="Water treatment filters and piping mounted on a wall"></div>
        <p>Lorem Ipsum is simply dummy text of the printing and typesetting industry. Lorem Ipsum has been the industry's standard dummy text ever since the 1500s, when an unknown printer took a galley of type and scrambled it to make a type specimen book. It has survived not only five centuries, but also the leap into electronic typesetting, remaining essentially unchanged. It was popularised in the 1960s with the release of Typeset sheets containing Lorem Ipsum passages, and more recently with desktop publishing software like Folio PageSetter including versions of Lorem Ipsum.</p>
        <p>It is a long established fact that a reader will be distracted by the readable content of a page when looking at its layout. The point of using Lorem Ipsum is that it has a more-or-less normal distribution of letters, as opposed to using 'Content here, content here', making it look like readable English. Many desktop publishing packages and web page editors now use Lorem Ipsum as their default model text, and a search for 'lorem ipsum' will uncover many web sites still in their infancy. Various versions have evolved over the years, sometimes by accident, sometimes on purpose (injected humour and the like).</p>
      </section>

      <section class="service-block second">
        <div class="service-photo left" role="img" aria-label="Wastewater treatment room with green pipework and tanks"></div>
        <p>Lorem Ipsum is simply dummy text of the printing and typesetting industry. Lorem Ipsum has been the industry's standard dummy text ever since the 1500s, when an unknown printer took a galley of type and scrambled it to make a type specimen book. It has survived not only five centuries, but also the leap into electronic typesetting, remaining essentially unchanged. It was popularised in the 1960s with the release of Typeset sheets containing Lorem Ipsum passages, and more recently with desktop publishing software like Folio PageSetter including versions of Lorem Ipsum.</p>
        <p>It is a long established fact that a reader will be distracted by the readable content of a page when looking at its layout. The point of using Lorem Ipsum is that it has a more-or-less normal distribution of letters, as opposed to using 'Content here, content here', making it look like readable English. Many desktop publishing packages and web page editors now use Lorem Ipsum as their default model text, and a search for 'lorem ipsum' will uncover many web sites still in their infancy. Various versions have evolved over the years, sometimes by accident, sometimes on purpose (injected humour and the like).</p>
      </section>
    </div>
  </main>

  <div class="water-band" role="img" aria-label="Rippling water surface with splashes along the page bottom"></div>
</div>
</body>
</html>
```